Kelvane Plumbing Business cards

Company is Kelvane Plumbing.
name Dashel Morrowby, I am a plumber, drainer, gasfitter and roofer
Mobile: 0431 906 154
Email address: info@kelvaneplumbing.example (check out my website for some ideas)
Website: www.kelvaneplumbing.example
ABN: 82 916 203 471
LIC: 604517K

I am reliable all round plumber. I am a 24 hour emergency service. Kelvane Plumbing is a professional plumbing service in the Illawarra, South Coast, Southern Sydney and Southern Highland regions of NSW. We offer a 24 hour emergency service for piece of mind to our customers. Call us now to see how we can help you. Kelvane Plumbing approaches every job with attention to detail and excellent customer service. With our superior workmanship you can be confident that the job will be done right the first time around. You can rest assured with results that are guaranteed to last.

Target Market(s)

the general public

Contact Information for Business Card

look up website for some ideas something with similar colours to logo and new modern and to catch the eye.

Colors
fdfdfd
ffffff
000000
7f7f7f
aaaaaa
33a6d7
0492cd

Requirements
Must have
• all contact details
• company- Kelvane Plumbing
• name- Dashel Morrowby
• number mobile- 0431 906 154
• Email address- info@kelvaneplumbing.example
• Website- www.kelvaneplumbing.example
• ABN- 82 916 203 471
• LIC- 604517K

```html
<!DOCTYPE html>
<html lang="en">
<head>
<meta charset="utf-8">
<title>Kelvane Plumbing — Business Cards</title>
<link rel="stylesheet" href="https://fonts.googleapis.com/css2?family=Roboto+Condensed:ital,wght@0,400;0,700;1,700&family=Montserrat:wght@700&display=swap">
<style>
  :root {
    --black: #000000;
    --blue: #33a6d7;
    --blue-deep: #0492cd;
    --grey: #7f7f7f;
    --grey-light: #aaaaaa;
    --card-grey: #e2e2e2;
    --stage: #ebebeb;
    --stage-frame: #f6f6f6;
    --white: #ffffff;
    --ink: #1b1b1b;
  }
  * { box-sizing: border-box; margin: 0; padding: 0; }
  html, body { width: 1052px; height: 1200px; overflow: hidden; }
  body {
    background: var(--stage);
    font-family: "Roboto Condensed", Arial, sans-serif;
    position: relative;
  }
  .stage-frame {
    position: absolute; inset: 28px;
    border: 3px solid var(--stage-frame);
  }
  .card {
    position: absolute; left: 160px; width: 732px; height: 430px;
    overflow: hidden;
    box-shadow: 3px 5px 8px rgba(0,0,0,.45);
  }
  .card--front { top: 137px; background: var(--card-grey); }
  .card--back { top: 625px; background: var(--black); }

  .front-shapes { position: absolute; inset: 0; }
  .brand-mark {
    position: absolute; left: 30px; top: 150px; width: 300px;
    text-align: center; color: var(--blue);
    font-family: "Montserrat", Arial, sans-serif; font-weight: 700;
  }
  .brand-mark__name { font-size: 44px; line-height: 1; letter-spacing: 1px; }
  .brand-mark__trade { font-size: 21px; letter-spacing: 9px; margin-top: 10px; }

  .identity { position: absolute; left: 438px; top: 56px; width: 270px; text-align: center; }
  .identity__company { color: var(--blue-deep); font-weight: 700; font-size: 29px; letter-spacing: .5px; }
  .identity__person { color: var(--grey); font-weight: 700; font-size: 21px; margin-top: 4px; letter-spacing: .5px; }

  .contacts { position: absolute; left: 432px; top: 262px; list-style: none; }
  .contacts li {
    display: flex; align-items: center; gap: 12px;
    height: 36px; font-size: 17px; font-weight: 700; font-style: italic; color: var(--ink);
  }
  .contacts svg { width: 18px; height: 18px; flex: none; }

  .back-band {
    position: absolute; left: 0; right: 0; bottom: 0; height: 130px;
    background: var(--card-grey);
  }
  .back-brand {
    position: absolute; left: 0; right: 0; top: 88px; text-align: center;
    color: var(--blue); font-family: "Montserrat", Arial, sans-serif; font-weight: 700;
  }
  .back-brand__name { font-size: 68px; line-height: 1; letter-spacing: 3px; }
  .back-brand__trade { font-size: 30px; letter-spacing: 18px; margin-top: 8px; padding-left: 18px; }

  .registration {
    position: absolute; left: 62px; bottom: 28px;
    font-weight: 700; font-style: italic; font-size: 21px; color: var(--ink); line-height: 36px;
  }
  .tools-art {
    position: absolute; left: 400px; bottom: 0; width: 310px; height: 160px;
    background: linear-gradient(180deg, #8fd0ea, #5fb6dc);
    opacity: .85;
  }
</style>
</head>
<body>
  <div class="stage-frame"></div>

  <section class="card card--front">
    <svg class="front-shapes" viewBox="0 0 732 430" width="732" height="430" aria-hidden="true">
      <circle cx="136" cy="215" r="256" fill="var(--blue-deep)"/>
      <circle cx="120" cy="215" r="236" fill="var(--black)"/>
      <rect x="354" y="188" width="68" height="17" rx="8.5" fill="var(--blue)"/>
      <rect x="354" y="220" width="68" height="17" rx="8.5" fill="var(--blue)"/>
    </svg>
    <div class="brand-mark">
      <div class="brand-mark__name">KELVANE</div>
      <div class="brand-mark__trade">PLUMBING</div>
    </div>
    <div class="identity">
      <h1 class="identity__company">KELVANE PLUMBING</h1>
      <p class="identity__person">Dashel Morrowby</p>
    </div>
    <ul class="contacts">
      <li>
        <svg viewBox="0 0 18 18"><rect x="5" y="1" width="8" height="16" rx="1.5" fill="none" stroke="var(--blue-deep)" stroke-width="2"/><circle cx="9" cy="14" r="1" fill="var(--blue-deep)"/></svg>
        0431 906 154
      </li>
      <li>
        <svg viewBox="0 0 18 18"><rect x="1" y="4" width="16" height="11" fill="none" stroke="var(--blue-deep)" stroke-width="2"/><path d="M1 4l8 6 8-6" fill="none" stroke="var(--blue-deep)" stroke-width="2"/></svg>
        info@kelvaneplumbing.example
      </li>
      <li>
        <svg viewBox="0 0 18 18"><path d="M3 2l12 6-5 2-2 5z" fill="var(--blue-deep)"/></svg>
        www.kelvaneplumbing.example
      </li>
    </ul>
  </section>

  <section class="card card--back">
    <div class="back-brand">
      <div class="back-brand__name">KELVANE</div>
      <div class="back-brand__trade">PLUMBING</div>
    </div>
    <div class="back-band"></div>
    <div class="tools-art" role="img" aria-label="Illustration of two crossed plumbing wrenches in light blue"></div>
    <div class="registration">
      <p>ABN- 82 916 203 471</p>
      <p>LIC- 604517K</p>
    </div>
  </section>
</body>
</html>
```